Design a business card & stationary for a mortgage company

We are looking for a good looking business card design for our mortgage company that includes our logo. We received a free design as part of our logo project but we don't love it. The company is called "Pinecrest Mortgage Company" so we like waves and lighthouses. The logo should be included. We have a version in both vertical and horizontal that we have provided.

Industry/Entity Type

Finance

Contact Information for Business Card

This should include our new logo file

Requirements
Must have
• 3. The details you'd like on the card - name, title, phone, email, website, address, social media handles etc.
1. Marcus Hale
Vice President
732-419-6253
Fax 888-304-2918
mhale@pinecrestmortgage.example
NMLS 47162 - Company NMLS 61290
18 Larkin Ave
Toms River, NJ 08614

```html
<!DOCTYPE html>
<html lang="en">
<head>
<meta charset="utf-8">
<title>Pinecrest Mortgage Company – Business Card</title>
<link href="https://fonts.googleapis.com/css2?family=Jost:wght@400;500&family=Arimo:wght@400&display=swap" rel="stylesheet">
<style>
  :root {
    --backdrop: #1d1d1f;
    --brand-navy: #17538f;
    --brand-blue: #1f64a6;
    --accent-sky: #1e96dc;
    --paper: #ffffff;
    --ink-light: #ffffff;
  }
  html, body {
    margin: 0;
    padding: 0;
    width: 1200px;
    height: 930px;
    overflow: hidden;
    background: var(--backdrop);
  }
  .canvas {
    position: relative;
    width: 1200px;
    height: 930px;
  }
  .card {
    position: absolute;
    width: 560px;
    height: 320px;
    border-radius: 18px;
    overflow: hidden;
  }

  /* Back of card */
  .card-back {
    left: 90px;
    top: 110px;
    background: linear-gradient(135deg, var(--brand-blue), var(--brand-navy));
    display: flex;
    align-items: center;
    justify-content: center;
  }
  .brand-lockup {
    display: flex;
    align-items: center;
    gap: 14px;
  }
  .brand-dot {
    width: 18px;
    height: 18px;
    border-radius: 50%;
  }
  .brand-name {
    font-family: "Jost", sans-serif;
    font-weight: 500;
    text-transform: uppercase;
    letter-spacing: 1px;
    margin: 0;
  }
  .card-back .brand-dot { background: var(--ink-light); }
  .card-back .brand-name { color: var(--ink-light); font-size: 27px; }

  /* Front of card */
  .card-front {
    left: 550px;
    top: 500px;
    background: var(--paper);
  }
  .wave {
    position: absolute;
    inset: 0;
    width: 100%;
    height: 100%;
  }
  .card-front .brand-lockup {
    position: absolute;
    right: 34px;
    top: 52px;
    gap: 10px;
  }
  .card-front .brand-dot { background: var(--brand-navy); width: 14px; height: 14px; }
  .card-front .brand-name { color: var(--brand-navy); font-size: 17px; }

  .person {
    position: absolute;
    left: 34px;
    top: 96px;
  }
  .person-name {
    font-family: "Jost", sans-serif;
    font-weight: 500;
    font-size: 24px;
    color: var(--brand-navy);
    text-transform: uppercase;
    margin: 0;
    line-height: 1;
  }
  .person-title {
    font-family: "Jost", sans-serif;
    font-weight: 400;
    font-size: 15px;
    line-height: 1.2;
    color: var(--accent-sky);
    margin: 3px 0 0 14px;
  }

  .contact {
    position: absolute;
    left: 96px;
    top: 206px;
    margin: 0;
    padding: 0;
    list-style: none;
    font-family: "Arimo", sans-serif;
    font-size: 13px;
    line-height: 15px;
    color: var(--ink-light);
  }
  .contact li {
    display: flex;
    align-items: center;
    gap: 7px;
  }
  .contact svg {
    width: 10px;
    height: 10px;
    flex: none;
    margin-left: -17px;
  }
</style>
</head>
<body>
<main class="canvas">

  <section class="card card-back" aria-label="Business card back">
    <div class="brand-lockup">
      <span class="brand-dot"></span>
      <p class="brand-name">Pinecrest Mortgage Company</p>
    </div>
  </section>

  <section class="card card-front" aria-label="Business card front">
    <svg class="wave" viewBox="0 0 560 320" preserveAspectRatio="none" aria-hidden="true">
      <path d="M0 200 C 140 172, 280 152, 400 154 S 530 132, 560 82 L560 320 L0 320 Z" fill="var(--brand-blue)"/>
      <path d="M0 190 C 140 162, 280 142, 400 144 S 530 122, 560 72" fill="none" stroke="var(--accent-sky)" stroke-width="7"/>
      <path d="M230 160 C 300 144, 350 138, 410 140 S 530 114, 560 64" fill="none" stroke="var(--brand-navy)" stroke-width="4"/>
    </svg>

    <div class="brand-lockup">
      <span class="brand-dot"></span>
      <p class="brand-name">Pinecrest Mortgage Company</p>
    </div>

    <div class="person">
      <h1 class="person-name">Marcus Hale</h1>
      <p class="person-title">Vice President</p>
    </div>

    <ul class="contact">
      <li>NMLS 47162</li>
      <li>Company NMLS 61290</li>
      <li>18 Larkin Ave Toms River, NJ 08614</li>
      <li>
        <svg viewBox="0 0 10 10" aria-hidden="true"><path d="M2 1 L4 1 L4.6 3.2 L3.4 4 C4 5.4 4.8 6.2 6 6.8 L6.8 5.6 L9 6.2 L9 8.2 C5 9 1 5 2 1 Z" fill="#fff"/></svg>
        <span>732-419-6253</span>
      </li>
      <li>
        <svg viewBox="0 0 10 10" aria-hidden="true"><rect x="2.5" y="0.5" width="5" height="3" fill="#fff"/><rect x="0.5" y="3.5" width="9" height="4" rx="1" fill="#fff"/><rect x="2.5" y="6.5" width="5" height="3" fill="#fff" stroke="var(--brand-blue)" stroke-width="0.6"/></svg>
        <span>888-304-2918</span>
      </li>
      <li>
        <svg viewBox="0 0 10 10" aria-hidden="true"><rect x="0.7" y="2" width="8.6" height="6" fill="none" stroke="#fff" stroke-width="1"/><path d="M0.7 2 L5 5.5 L9.3 2" fill="none" stroke="#fff" stroke-width="1"/></svg>
        <span>mhale@pinecrestmortgage.example</span>
      </li>
      <li>
        <svg viewBox="0 0 10 10" aria-hidden="true"><circle cx="5" cy="5" r="4.3" fill="none" stroke="#fff" stroke-width="1"/><ellipse cx="5" cy="5" rx="1.8" ry="4.3" fill="none" stroke="#fff" stroke-width="0.8"/><path d="M0.7 5 H9.3" stroke="#fff" stroke-width="0.8"/></svg>
        <span>www.pinecrestmortgage.example</span>
      </li>
    </ul>
  </section>

</main>
</body>
</html>
```